Business card design and logo needed

We have been operating as Ridgeline Posts for 30 years but never had a logo and feel there is a need for one, but have no idea for a design.
We specialise in all types of rural fencing including post and wire, post and rail, electric, chainmesh and to a lesser extent, also do industrial security fencing.
Updates

Sorry, but website is ridgelineposts.example

No .au on the end!
My apologies

Regards, Darren

Target Market(s)

Rural/acreage property owners, particularly horse people.

Industry/Entity Type

Industrial

Contact Information for Business Card

Ridgeline Posts Darren Kellett 0499 572106. Lewis Kellett 0499 613720
Email: ridgelineposts@mailhub.example
Website: www.ridgelineposts.example.au

Requirements
Must have
• Would like to highlight website address - use the business card to advertise the website or to push them to check it out.

```html
<!DOCTYPE html>
<html lang="en">
<head>
<meta charset="utf-8">
<title>Ridgeline Posts – Business Card</title>
<link rel="stylesheet" href="https://fonts.googleapis.com/css2?family=Roboto+Slab:wght@300&display=swap">
<style>
  :root {
    --ink: #1c1c1c;
    --rule: #6e6e6e;
    --timber-light: #f1f1f0;
    --timber-mid: #e2e2e1;
    --timber-dark: #d4d4d3;
  }
  html, body {
    margin: 0;
    padding: 0;
    width: 1200px;
    height: 685px;
    overflow: hidden;
    background: #ffffff;
  }
  .card {
    position: relative;
    width: 1200px;
    height: 685px;
    overflow: hidden;
    font-family: "Roboto Slab", serif;
    font-weight: 300;
    color: var(--ink);
  }
  .timber-backdrop {
    position: absolute;
    inset: 0;
    background: linear-gradient(172deg, var(--timber-light) 0%, var(--timber-mid) 45%, var(--timber-light) 70%, var(--timber-dark) 100%);
  }
  .brand-mark {
    position: absolute;
    left: 47px;
    top: 46px;
    width: 346px;
    height: 346px;
  }
  .brand-mark svg {
    position: absolute;
    inset: 0;
  }
  .brand-name {
    position: absolute;
    inset: 0;
    display: flex;
    align-items: center;
    justify-content: center;
    text-align: center;
    font-size: 44px;
    line-height: 1.15;
    color: var(--ink);
  }
  .contact {
    position: absolute;
    left: 585px;
    top: 266px;
    margin: 0;
    line-height: 1;
  }
  .company {
    font-size: 35px;
    margin: 0 0 24px;
  }
  .person, .email {
    margin: 0;
    font-size: 37px;
    height: 52px;
  }
  .email {
    font-size: 34px;
  }
  .website {
    position: absolute;
    left: 585px;
    width: 577px;
    top: 546px;
    height: 66px;
    border-top: 2px solid var(--rule);
    border-bottom: 2px solid var(--rule);
    box-sizing: border-box;
    display: flex;
    align-items: center;
    font-size: 31px;
    letter-spacing: 0.2px;
    margin: 0;
  }
</style>
</head>
<body>
  <main class="card">
    <div class="timber-backdrop" role="img" aria-label="Pale whitewashed timber grain background"></div>

    <div class="brand-mark">
      <svg width="346" height="346" viewBox="0 0 346 346" aria-hidden="true">
        <circle cx="173" cy="173" r="170" fill="none" stroke="var(--ink)" stroke-width="4"/>
      </svg>
      <div class="brand-name">Ridgeline<br>Posts</div>
    </div>

    <section class="contact">
      <p class="company">Ridgeline Posts</p>
      <p class="person">Darren Kellett 0499 572106</p>
      <p class="person">Lewis Kellett 0499 613720</p>
      <p class="email">ridgelineposts@mailhub.example</p>
    </section>

    <p class="website">WWW.RIDGELINEPOSTS.EXAMPLE</p>
  </main>
</body>
</html>
```